Brenner & Holloway Stationery

Greetings again. Now we've got an awesome logo, it's time to get the stationery to go with it. We require the following items of stationery:

- Business Card - Print Ready, all we need to do is change names and numbers and submit to printer.  Double sided with logo on one side and details on the other side. (85mm x 55mm)

- With Compliments Slip

- Letterhead - These will be preprinted pages that will then be used as pages.
(A4)

- Envelope - Business Size(Standard DL)

Target Market(s)

Essentially, this firm services clients facing criminal charges and/or seeking legal aid. The firm is also looking at taking on more white-collar crime cases.

Requirements
Must have
• - Same Design Cues & Colours as the Branding details attached

• - Address (as follows)

• Suite 8

• 262-268 Marlow St

• DANDENONG VIC 3175

• Phone: (03) 9482 6315

• Fax: (03) 9482 6840

• Web: www.brennerandholloway.example.au

• - Colour: Pantone 194 (Red)

```html
<!DOCTYPE html>
<html lang="en">
<head>
<meta charset="utf-8">
<title>Brenner &amp; Holloway Stationery</title>
<link rel="stylesheet" href="https://fonts.googleapis.com/css2?family=Cinzel:wght@400;600&family=Questrial&display=swap">
<style>
  :root {
    --brand-red: #a8073a;
    --ink: #111111;
    --rule: #9a9a9a;
    --body-grey: #5e5e5e;
    --paper: #ffffff;
    --shadow: 0 6px 14px rgba(0,0,0,0.35);
  }
  * { margin: 0; padding: 0; box-sizing: border-box; }
  html, body { width: 1200px; height: 946px; overflow: hidden; background: var(--paper); }
  .canvas { position: relative; width: 1200px; height: 946px; font-family: 'Cinzel', serif; color: var(--ink); }

  .brand { position: absolute; display: flex; align-items: center; }
  .brand-mark { border-radius: 50%; background: var(--brand-red); flex: none; }
  .brand-rule { width: 1px; background: var(--rule); flex: none; }
  .brand-name { font-weight: 600; line-height: 1; white-space: nowrap; }
  .brand-tag { line-height: 1; white-space: nowrap; letter-spacing: 0.12em; margin-top: 0.15em; }

  .piece { position: absolute; background: var(--paper); box-shadow: var(--shadow); overflow: hidden; }

  /* master logo */
  .logo-master { left: 98px; top: 110px; }
  .logo-master .brand-mark { width: 94px; height: 94px; }
  .logo-master .brand-rule { height: 94px; margin: 0 19px 0 18px; }
  .logo-master .brand-name { font-size: 25px; }
  .logo-master .brand-tag { font-size: 15.5px; margin-top: 6px; }

  /* business card front */
  .card-front { left: 36px; top: 255px; width: 254px; height: 150px; }
  .card-front .brand { left: 19px; top: 29px; }
  .card-front .brand-mark { width: 56px; height: 56px; }
  .card-front .brand-rule { height: 56px; margin: 0 10px 0 4px; }
  .card-front .brand-name { font-size: 13.5px; }
  .card-front .brand-tag { font-size: 8.3px; letter-spacing: 0.1em; }

  /* business card back */
  .card-back { left: 323px; top: 255px; width: 254px; height: 150px; background: var(--brand-red); color: #fff; }
  .card-holder { position: absolute; right: 167px; top: 66px; text-align: center; line-height: 1; }
  .card-holder .holder-name { font-size: 9.5px; letter-spacing: 0.05em; }
  .card-holder .holder-role { font-size: 6.5px; letter-spacing: 0.1em; margin-top: 2px; }
  .card-back .card-rule { position: absolute; left: 95px; top: 37px; width: 1px; height: 74px; background: rgba(255,255,255,0.7); }
  .card-details { position: absolute; left: 106px; top: 35px; font-size: 8px; line-height: 11px; letter-spacing: 0.02em; white-space: nowrap; }
  .card-details .gap { height: 11px; }
  .card-details .web { font-size: 5px; letter-spacing: 0; }

  /* envelope */
  .envelope-flap { position: absolute; left: 74px; top: 440px; width: 456px; height: 36px; background: var(--brand-red); clip-path: polygon(5% 0, 95% 0, 100% 100%, 0 100%); }
  .envelope { left: 74px; top: 475px; width: 456px; height: 197px; border: 1px solid #444; }
  .envelope .brand { left: 19px; top: 21px; }
  .envelope-window { position: absolute; left: 268px; top: 119px; width: 153px; height: 42px; border: 1px solid #333; border-radius: 12px; }
  .foot-band { position: absolute; left: 0; right: 0; bottom: 0; height: 5px; background: var(--brand-red); }

  .small-brand .brand-mark { width: 36px; height: 36px; }
  .small-brand .brand-rule { height: 36px; margin: 0 5px 0 4px; }
  .small-brand .brand-name { font-size: 10px; }
  .small-brand .brand-tag { font-size: 6.4px; letter-spacing: 0.06em; }
  .mini-address { position: absolute; font-size: 5.2px; line-height: 9.6px; letter-spacing: 0.03em; }

  .envelope .mini-address { left: 69px; top: 56px; }

  /* compliments slip */
  .comp-slip { left: 74px; top: 714px; width: 456px; height: 198px; border: 1px solid #444; }
  .comp-slip .brand { left: 12px; top: 22px; }
  .comp-slip .mini-address { left: 63px; top: 55px; }
  .comp-label { position: absolute; left: 366px; top: 45px; font-size: 5.4px; letter-spacing: 0.06em; }

  /* letterhead */
  .letterhead { left: 616px; top: 84px; width: 573px; height: 827px; }
  .letterhead .brand { left: 88px; top: 39px; }
  .letterhead .brand-mark { width: 48px; height: 48px; }
  .letterhead .brand-rule { height: 48px; margin: 0 9px 0 7px; }
  .letterhead .brand-name { font-size: 13px; }
  .letterhead .brand-tag { font-size: 7.8px; letter-spacing: 0.1em; }
  .letter-body { position: absolute; left: 98px; top: 188px; width: 424px; font-family: 'Questrial', sans-serif; font-size: 9.2px; line-height: 24.3px; color: var(--body-grey); }
  .letter-body p + p { margin-top: 24.3px; }
  .letter-rule { position: absolute; left: 82px; top: 712px; width: 1px; height: 86px; background: var(--rule); }
  .letter-address { position: absolute; left: 95px; top: 711px; font-size: 6.6px; line-height: 12.8px; letter-spacing: 0.03em; white-space: nowrap; }
  .letter-address .gap { height: 12.8px; }
  .letterhead .foot-band { height: 7px; }
</style>
</head>
<body>
<div class="canvas">

  <div class="brand logo-master">
    <div class="brand-mark"></div>
    <div class="brand-rule"></div>
    <div class="brand-text">
      <div class="brand-name">Brenner &amp; Holloway</div>
      <div class="brand-tag">BARRISTERS &amp; SOLICITORS</div>
    </div>
  </div>

  <section class="piece card-front">
    <div class="brand">
      <div class="brand-mark"></div>
      <div class="brand-rule"></div>
      <div class="brand-text">
        <div class="brand-name">Brenner &amp; Holloway</div>
        <div class="brand-tag">BARRISTERS &amp; SOLICITORS</div>
      </div>
    </div>
  </section>

  <section class="piece card-back">
    <div class="card-holder">
      <div class="holder-name">DANIEL WARD</div>
      <div class="holder-role">PARTNER</div>
    </div>
    <div class="card-rule"></div>
    <div class="card-details">
      <div>Suite 8</div>
      <div>262-268 Marlow St</div>
      <div>DANDENONG VIC 3175</div>
      <div class="gap"></div>
      <div>Phone: (03) 9482 6315</div>
      <div>Fax: (03) 9482 6840</div>
      <div class="web">WWW.BRENNERANDHOLLOWAY.EXAMPLE.AU</div>
    </div>
  </section>

  <div class="envelope-flap"></div>
  <section class="piece envelope">
    <div class="brand small-brand">
      <div class="brand-mark"></div>
      <div class="brand-rule"></div>
      <div class="brand-text">
        <div class="brand-name">Brenner &amp; Holloway</div>
        <div class="brand-tag">BARRISTERS &amp; SOLICITORS</div>
      </div>
    </div>
    <div class="mini-address">
      <div>Suite 8</div>
      <div>262-268 Marlow St</div>
      <div>DANDENONG VIC 3175</div>
    </div>
    <div class="envelope-window"></div>
    <div class="foot-band"></div>
  </section>

  <section class="piece comp-slip">
    <div class="brand small-brand">
      <div class="brand-mark"></div>
      <div class="brand-rule"></div>
      <div class="brand-text">
        <div class="brand-name">Brenner &amp; Holloway</div>
        <div class="brand-tag">BARRISTERS &amp; SOLICITORS</div>
      </div>
    </div>
    <div class="mini-address">
      <div>Suite 8</div>
      <div>262-268 Marlow St</div>
      <div>DANDENONG VIC 3175</div>
    </div>
    <div class="comp-label">with compliments</div>
    <div class="foot-band"></div>
  </section>

  <section class="piece letterhead">
    <div class="brand">
      <div class="brand-mark"></div>
      <div class="brand-rule"></div>
      <div class="brand-text">
        <div class="brand-name">Brenner &amp; Holloway</div>
        <div class="brand-tag">BARRISTERS &amp; SOLICITORS</div>
      </div>
    </div>
    <div class="letter-body">
      <p>Lorem ipsum dolor sit amet, consectetur adipisicing elit, sed do eiusmod tempor incididunt ut labore et dolore magna aliqua. Ut enim ad minim veniam, quis nostrud exercitation ullamco laboris nisi ut aliquip ex ea commodo consequat. Duis aute irure dolor in reprehenderit in voluptate velit esse cillum dolore eu fugiat nulla pariatur. Excepteur sint occaecat cupidatat non proident, sunt in culpa qui officia deserunt mollit anim id est laborum Lorem ipsum dolor sit amet, consectetur adipisicing elit, sed do eiusmod tempor incididunt ut labore et dolore magna aliqua. Ut enim ad minim veniam, quis nostrud exercitation ullamco laboris nisi ut aliquip ex ea commodo consequat. Duis aute irure dolor in reprehenderit in voluptate velit esse cillum dolore eu fugiat nulla pariatur. Excepteur sint occaecat cupidatat non proident, sunt in culpa qui officia deserunt mollit anim id est laborum</p>
      <p>Lorem ipsum dolor sit amet, consectetur adipisicing elit, sed do eiusmod tempor incididunt ut labore et dolore magna aliqua. Ut enim ad minim veniam, quis nostrud exercitation ullamco laboris nisi ut aliquip ex ea commodo consequat. Duis aute irure dolor in reprehenderit in voluptate velit esse cillum dolore eu fugiat nulla pariatur. Excepteur sint occaecat cupidatat non proident, sunt in culpa qui officia deserunt mollit anim id est laborum</p>
    </div>
    <div class="letter-rule"></div>
    <div class="letter-address">
      <div>Suite 8</div>
      <div>262-268 Marlow St</div>
      <div>DANDENONG VIC 3175</div>
      <div class="gap"></div>
      <div>Phone: (03) 9482 6315</div>
      <div>Fax: (03) 9482 6840</div>
      <div>www.brennerandholloway.example.au</div>
    </div>
    <div class="foot-band"></div>
  </section>

</div>
</body>
</html>
```